Mesh Banner Design for Business Premises

We require the design of a large mesh banner to be installed across the front fence of our warehouse. The banner should prominently feature our existing Rigmore logo and brand colours (yellow, white, and black) and be designed to be highly visible from the road.

The overall aesthetic should be strong, masculine, and industrial, reflecting the nature of the scaffolding and construction industry. The background should be predominantly black, with our branding incorporated in yellow and white for strong contrast and readability.

The banner should clearly communicate the full scope of services we provide, including:

Scaffold Design
Scaffold Engineering
Scaffold Installation / Erection
Scaffold Dismantling

It should also indicate the types of projects and clients we service, including:

Commercial
Industrial
Residential
Civil

The design should feel bold and professional, with a construction-oriented style that aligns with the scaffolding industry. It should be clean, impactful, and easy to read from a distance, ensuring passing traffic can quickly understand our services.

Where possible, subtle industrial or structural design elements (such as scaffold components, steel textures, or linework) may be incorporated into the background to reinforce the industry theme while keeping the layout uncluttered.

The final design will be produced as a large-format mesh banner for outdoor installation, so it should be created with this application and viewing distance in mind.

```html
<!DOCTYPE html>
<html lang="en">
<head>
<meta charset="utf-8">
<title>Rigmore – Scaffolding Banner</title>
<link rel="stylesheet" href="https://fonts.googleapis.com/css2?family=Teko:wght@500&family=Montserrat:wght@300;500&display=swap">
<style>
  :root {
    --ink: #000000;
    --amber: #e8993a;
    --white: #ffffff;
    --steel-dark: #2a2c2e;
    --steel-mid: #5d6062;
    --steel-light: #9aa0a3;
  }
  html, body {
    margin: 0;
    padding: 0;
    width: 1200px;
    height: 343px;
    overflow: hidden;
    background: var(--ink);
  }
  .banner {
    display: block;
    width: 1200px;
    height: 343px;
  }
  .service {
    font-family: "Teko", "Arial Narrow", sans-serif;
    font-weight: 500;
    font-size: 46px;
  }
  .sector {
    font-family: "Teko", "Arial Narrow", sans-serif;
    font-weight: 500;
    font-size: 32px;
    fill: var(--white);
  }
  .is-white { fill: var(--white); }
  .is-amber { fill: var(--amber); }
  .sector-icon { fill: var(--amber); }
  .brand-name {
    font-family: "Montserrat", Arial, sans-serif;
    font-weight: 500;
    font-size: 20px;
    fill: var(--white);
  }
  .brand-phone {
    font-family: "Montserrat", Arial, sans-serif;
    font-weight: 300;
    font-size: 48px;
    fill: var(--white);
  }
</style>
</head>
<body>
<svg class="banner" viewBox="0 0 1200 343" xmlns="http://www.w3.org/2000/svg">
  <defs>
    <linearGradient id="site-tones" x1="0" y1="0" x2="0" y2="1">
      <stop offset="0" stop-color="var(--steel-light)"/>
      <stop offset="0.45" stop-color="var(--steel-mid)"/>
      <stop offset="1" stop-color="var(--steel-dark)"/>
    </linearGradient>
  </defs>

  <rect class="backdrop" width="1200" height="343" fill="var(--ink)"/>

  <!-- central chevron with site photo -->
  <polygon class="chevron-frame" points="380,0 879,0 626,343" fill="var(--amber)"/>
  <polygon class="chevron-photo" points="409,0 855,0 626,315" fill="url(#site-tones)"
           role="img" aria-label="Photo of a warehouse interior lined with multi-level scaffolding"/>

  <!-- services list -->
  <g class="services">
    <text class="service is-white" x="145" y="82" textLength="233" lengthAdjust="spacingAndGlyphs">SCAFFOLD DESIGN</text>
    <text class="service is-amber" x="120" y="152" textLength="304" lengthAdjust="spacingAndGlyphs">SCAFFOLD DISMANTLING</text>
    <text class="service is-white" x="159" y="221" textLength="312" lengthAdjust="spacingAndGlyphs">SCAFFOLD ENGINEERING</text>
    <text class="service is-amber" x="56" y="293" textLength="456" lengthAdjust="spacingAndGlyphs">SCAFFOLD INSTALLATION / ERECTION</text>
  </g>

  <!-- sectors list -->
  <g class="sectors">
    <text class="sector" x="1110" y="72" text-anchor="end">COMMERCIAL</text>
    <g class="sector-icon">
      <rect x="1126" y="42" width="9" height="30"/>
      <rect x="1133" y="38" width="20" height="34"/>
    </g>

    <text class="sector" x="1110" y="112" text-anchor="end">INDUSTRIAL</text>
    <g class="sector-icon">
      <rect x="1126" y="96" width="12" height="16"/>
      <rect x="1138" y="84" width="15" height="28"/>
    </g>

    <text class="sector" x="1110" y="153" text-anchor="end">RESIDENTIAL</text>
    <g class="sector-icon">
      <polygon points="1124,141 1140,129 1156,141"/>
      <rect x="1128" y="141" width="24" height="11"/>
      <circle cx="1157" cy="145" r="3"/>
    </g>

    <text class="sector" x="1110" y="193" text-anchor="end">CIVIL</text>
    <g class="sector-icon">
      <rect x="1137" y="161" width="6" height="6"/>
      <rect x="1130" y="167" width="20" height="24"/>
      <rect x="1126" y="189" width="28" height="3"/>
    </g>
  </g>

  <!-- brand block -->
  <g class="brand">
    <rect class="brand-mark" x="762" y="242" width="48" height="48" fill="var(--amber)"/>
    <text class="brand-name" x="895" y="246" textLength="254" lengthAdjust="spacing">RIGMORE</text>
    <text class="brand-phone" x="886" y="299" textLength="270" lengthAdjust="spacingAndGlyphs">1300 7 HOIST</text>
  </g>
</svg>
</body>
</html>
```